Bus Card for Organic Hydroponic Produce company

We need a business card for a budding new business. We grow 100% organic, 100% hydroponic, 100% GMO free produce for sale in our local area. We need something bold and dynamic, not simple and elegant. We want to catch peoples attention and get them to visit our website to view more information about our products and services. Its difficult to explain on a business card the differences between our produce (tomatoes, cucumbers, peppers, etc...) and the kind they would buy at the local grocer or market. , so we need to push them to the website.
We have been brainstorming names for the company and have a few in mind, so choose whichever speaks most to your artistic flair and propose a card based on that one, or both. #1 "Tidewell Organics" with a slogan something like....." When merely growing green merely falls short" OR #2 "Brightmark Organics" with a slogan similar to...."The cutting edge in cleaner, purer organics" OR #3" "Hearthroot Organics" with a slogan similar to: "Building a healthier future for those we leave behind"" OR #4 "Verdant Accord" with a slogan similar to: "Purity by Simplicity"
Eventually we will need assistance with web design, promotional and sales materials, etc. so if you offer those services, please indicate that with the design, though it is NOT necessary to offer any additional services to win this contest. WE will pick the winner solely on the business card we like the most.
We want something that stands out, and especially with the name "Mabel's organics", we understand that a creative mind may wander into certain attention getting means that may not be quite within the realm of what we can hand out at our local grocer or farmers market. We definitely are not opposed to a little salacious undertone or allusion to attract attention, but please keep it tasteful if you skirt that grey area.
For our card, we use an online printer that can add foils, special die cuts, double sided cards, 3-d cards (we love these 32 pt cards), transparent or translucent cards and more. We love cards that have some of these things where possible and on all of our other business' cards we get rave reviews from customers about their uniqueness. plumfold-prints.example has the info on these accents if you wish to view what I am referencing.
So in conclusion, we want a unique, stylish, bold, vivid, 2 sided business card that will really stand out. Just usw a generic phone number and website for now and we will add them as they become available. Please email with any questions! Thanks in advance for your effort and creativity!
Target Market(s)
We are targeting parents who are conceintous of what their children and families are eating. Our target audience are moms, but we don't want to exclude anyone else who chooses to eat more healthy. Our target customer is the same customer that would shop at Greenbasket Market stores or local farmers markets

```html
<!DOCTYPE html>
<html lang="en">
<head>
<meta charset="utf-8">
<title>Coastfield Organics – Business Card</title>
<link rel="stylesheet" href="https://fonts.googleapis.com/css2?family=Caladea:wght@400;700&display=swap">
<style>
  :root {
    --backdrop: #e6f1e6;
    --brand-green: #0a8442;
    --brand-green-deep: #056b34;
    --leaf-light: #6cc070;
    --leaf-pale: #9fd59a;
    --ink-green: #17693a;
    --ink-dark: #111111;
    --card-white: #ffffff;
    --card-shadow: rgba(20, 60, 30, 0.22);
  }
  * { box-sizing: border-box; margin: 0; padding: 0; }
  html, body {
    width: 1200px;
    height: 900px;
    overflow: hidden;
    background: var(--backdrop);
    font-family: "Caladea", Cambria, Georgia, serif;
  }
  .sheet {
    width: 1200px;
    height: 900px;
    display: flex;
    align-items: center;
    justify-content: center;
    gap: 40px;
  }
  .card {
    position: relative;
    width: 540px;
    height: 315px;
    border-radius: 22px;
    overflow: hidden;
    box-shadow: 0 12px 30px var(--card-shadow);
  }

  /* Front */
  .card--front {
    background: linear-gradient(155deg, var(--brand-green) 0%, var(--brand-green-deep) 100%);
    color: var(--card-white);
  }
  .front__mark {
    position: absolute;
    left: -46px;
    bottom: -46px;
    width: 200px;
    height: 200px;
    border-radius: 50%;
    background: var(--leaf-pale);
    opacity: 0.5;
  }
  .front__text {
    position: absolute;
    right: 48px;
    top: 112px;
    text-align: right;
  }
  .front__name {
    font-size: 33px;
    font-weight: 400;
    letter-spacing: 0.6px;
    line-height: 1;
    white-space: nowrap;
  }
  .front__slogan {
    margin-top: 10px;
    font-size: 17px;
    letter-spacing: 0.2px;
    white-space: nowrap;
  }

  /* Back */
  .card--back {
    background: var(--card-white);
  }
  .back__mark {
    position: absolute;
    right: -60px;
    bottom: -70px;
    width: 230px;
    height: 230px;
    border-radius: 50%;
    background: var(--leaf-pale);
    opacity: 0.2;
  }
  .back__brand {
    position: absolute;
    top: 34px;
    right: 36px;
    display: flex;
    align-items: center;
    gap: 12px;
    color: var(--leaf-light);
  }
  .back__brand-dot {
    width: 26px;
    height: 26px;
    border-radius: 50%;
    background: var(--leaf-light);
  }
  .back__brand-name {
    font-size: 22px;
    letter-spacing: 0.5px;
    white-space: nowrap;
  }
  .back__contacts {
    position: absolute;
    right: 36px;
    bottom: 40px;
    list-style: none;
    text-align: right;
    font-size: 17px;
    line-height: 1.45;
    color: var(--ink-green);
    font-weight: 700;
    white-space: nowrap;
  }
  .back__label {
    color: var(--ink-dark);
    font-weight: 700;
  }
</style>
</head>
<body>
  <main class="sheet">
    <section class="card card--front" aria-label="Card front">
      <div class="front__mark"></div>
      <div class="front__text">
        <h1 class="front__name">COASTFIELD ORGANICS</h1>
        <p class="front__slogan">The region’s purest organic produce</p>
      </div>
    </section>

    <section class="card card--back" aria-label="Card back">
      <div class="back__mark"></div>
      <div class="back__brand">
        <span class="back__brand-dot"></span>
        <span class="back__brand-name">COASTFIELD ORGANICS</span>
      </div>
      <ul class="back__contacts">
        <li>555-555-5555 <span class="back__label">- Phone</span></li>
        <li>mabelsorganics@mailbox.example <span class="back__label">- E-Mail</span></li>
        <li>www.MabelsOrganics.example <span class="back__label">- Website</span></li>
        <li>48 Orchard Lane, Harborview, VA 23400 <span class="back__label">- Address</span></li>
      </ul>
    </section>
  </main>
</body>
</html>
```